Brightstone Roofing Business Card

This is my current business card. But I’d like to make some changes. Somewhere on the card I’d like to list some of the services we offer. Maybe on the back? But I’d still like to keep the red. White and black modern look.

-residential & commercial roofing
-Roof Repairs & Maintenance
-Storm Damage & Insurance Claims specialist
-Christmas Lights and permanent Christmas lights
Fencing. Windows. Gutters. Siding. Sheetrock, painting.

```html
<!DOCTYPE html>
<html lang="en">
<head>
<meta charset="utf-8">
<title>Brightstone Roofing Business Card</title>
<link href="https://fonts.googleapis.com/css2?family=Audiowide&family=Montserrat:wght@400;500&display=swap" rel="stylesheet">
<style>
  :root {
    --backdrop: #d2d3d5;
    --red: #e31e24;
    --deep-red: #6b0d10;
    --black: #111111;
    --white: #ffffff;
    --ink: #1b1b1b;
  }
  * { margin: 0; padding: 0; box-sizing: border-box; }
  html, body { width: 900px; height: 1200px; overflow: hidden; }
  body { background: var(--backdrop); position: relative; font-family: "Montserrat", sans-serif; }

  .card {
    position: absolute;
    left: 120px;
    width: 660px;
    height: 376px;
    border-radius: 16px;
    overflow: hidden;
  }
  .card-front { top: 204px; }
  .card-back { top: 622px; background: var(--white); }

  .tartan-fill {
    position: absolute; inset: 0;
    background:
      linear-gradient(180deg, transparent 0 24%, rgba(255,255,255,.35) 24% 30%, transparent 30% 45%, rgba(0,0,0,.75) 45% 66%, transparent 66%),
      linear-gradient(90deg, var(--deep-red) 0%, var(--red) 25%, var(--deep-red) 45%, var(--red) 70%, var(--deep-red) 100%);
  }
  .front-badge {
    position: absolute; left: 253px; top: 72px;
    width: 154px; height: 154px; border-radius: 50%;
    border: 4px solid var(--white);
  }
  .front-name {
    position: absolute; left: 0; right: 0; top: 240px;
    text-align: center; color: var(--white);
    font-family: "Audiowide", sans-serif; font-weight: 400;
    line-height: 1.15;
  }
  .front-name .line-main { display: block; font-size: 36px; }
  .front-name .line-sub { display: block; font-size: 26px; }

  .back-badge {
    position: absolute; left: 86px; top: 22px;
    width: 116px; height: 116px; border-radius: 50%;
    background: var(--red);
  }
  .back-name {
    position: absolute; left: 26px; width: 236px; top: 148px;
    text-align: center; color: var(--black);
    font-family: "Audiowide", sans-serif; line-height: 1.1;
  }
  .back-name .line-main { display: block; font-size: 28px; }
  .back-name .line-sub { display: block; font-size: 20px; }

  .person { position: absolute; left: 36px; top: 236px; }
  .person-name { font-family: "Audiowide", sans-serif; font-size: 24px; color: var(--black); letter-spacing: 1px; }
  .person-name .surname { color: var(--red); }
  .person-role { font-size: 14px; color: var(--ink); margin-top: 0; }

  .contacts { position: absolute; left: 36px; top: 292px; list-style: none; }
  .contacts li { display: flex; align-items: center; gap: 8px; font-size: 14.5px; color: var(--ink); height: 24px; }
  .contacts svg { width: 14px; height: 14px; flex: none; }

  .services { position: absolute; right: 26px; top: 38px; list-style: none; text-align: right; }
  .services li { position: relative; font-size: 14.5px; line-height: 18px; color: var(--ink); padding-right: 14px; margin-bottom: 4px; }
  .services li::after {
    content: ""; position: absolute; right: 0; top: 6px;
    width: 6px; height: 6px; border-radius: 50%; background: var(--red);
  }

  .feature-circle {
    position: absolute; left: 438px; top: 182px;
    width: 192px; height: 192px; border-radius: 50%;
    background: var(--red);
  }
  .bottom-band {
    position: absolute; left: 0; right: 0; bottom: 0; height: 8px;
    background: linear-gradient(90deg, var(--deep-red), var(--red), var(--deep-red));
  }
</style>
</head>
<body>

<section class="card card-front">
  <div class="tartan-fill" role="img" aria-label="Red, black and white tartan pattern"></div>
  <div class="front-badge"></div>
  <div class="front-name">
    <span class="line-main">BRIGHTSTONE</span>
    <span class="line-sub">ROOFING CO.</span>
  </div>
</section>

<section class="card card-back">
  <div class="back-badge"></div>
  <div class="back-name">
    <span class="line-main">BRIGHTSTONE</span>
    <span class="line-sub">ROOFING CO.</span>
  </div>

  <div class="person">
    <div class="person-name">DEAN <span class="surname">CARVER</span></div>
    <div class="person-role">Owner</div>
  </div>

  <ul class="contacts">
    <li>
      <svg viewBox="0 0 24 24"><path fill="#e31e24" d="M6.6 10.8a15 15 0 0 0 6.6 6.6l2.2-2.2c.3-.3.7-.4 1-.2 1.1.4 2.3.6 3.6.6.6 0 1 .4 1 1V20c0 .6-.4 1-1 1A17 17 0 0 1 3 4c0-.6.4-1 1-1h3.5c.6 0 1 .4 1 1 0 1.3.2 2.5.6 3.6.1.3 0 .7-.2 1z"/></svg>
      682-555-0148
    </li>
    <li>
      <svg viewBox="0 0 24 24"><rect x="2" y="5" width="20" height="14" rx="2" fill="#e31e24"/><path d="M3 6l9 7 9-7" fill="none" stroke="#fff" stroke-width="1.8"/></svg>
      dean@brightstoneroofing.com
    </li>
    <li>
      <svg viewBox="0 0 24 24"><circle cx="12" cy="12" r="10" fill="#e31e24"/><path d="M2 12h20M12 2c3 3 3 17 0 20M12 2c-3 3-3 17 0 20" fill="none" stroke="#fff" stroke-width="1.4"/></svg>
      www.brightstoneroofing.com
    </li>
  </ul>

  <ul class="services">
    <li>residential &amp; commercial roofing</li>
    <li>Roof Repairs &amp; Maintenance</li>
    <li>Storm Damage &amp;<br>Insurance Claims specialist</li>
    <li>Fencing. Windows. Gutters.<br>Siding. Sheetrock, painting</li>
  </ul>

  <div class="feature-circle"></div>
  <div class="bottom-band" role="img" aria-label="Thin red tartan strip"></div>
</section>

</body>
</html>
```